Halden Construction Inc Business Card Design

We want a business card that stands out; we build high end commercial interiors so card should be professional yet creative and have an architectural/design feel , very clean lines

We have 6 employees so we must be able to change the name, cell and email on each person's card
For the proof Paul Merriton is the president
Office Number is (555) 284-3916, Cell ( 555 ) 431-0827

4700 Calloway Lane Suite 305, Cedar Bay Gardens, FL 33918
www.haldenbuilds.com
CGC 374915 ( This license must legally be on card)

Target Market(s)

Asset Specialists , Developers, Building owners, architects, business owners

Industry/Entity Type

Construction Company

Contact Information for Business Card

We want a very high end clean look, must incorporate existing logo

Font styles to use
Other font styles liked:
• Gotham, trade gothic, Mrs. Eaves,modern 20, trim or designers' choice

Colors

Designer to choose colors to be used in the design.

Requirements
Must have
• Name, address, CGC 374915, www.haldenbuilds.com
• 4700 Calloway Lane Suite 305, Cedar Bay Gardens, FL 33918
• each persons name, cell phone and individual email address ie paulm@haldenbuilds.com

```html
<!DOCTYPE html>
<html lang="en">
<head>
<meta charset="utf-8">
<title>Halden Construction Inc — Business Card</title>
<link href="https://fonts.googleapis.com/css2?family=Montserrat:wght@500;600;700&display=swap" rel="stylesheet">
<style>
  :root {
    --backdrop: #ebebeb;
    --navy: #2b2c6e;
    --green: #6cc04a;
    --white: #ffffff;
  }
  * { margin: 0; padding: 0; box-sizing: border-box; }
  html, body {
    width: 1200px; height: 1000px; overflow: hidden;
    background: var(--backdrop);
    font-family: "Montserrat", Arial, sans-serif;
  }
  .card {
    position: absolute;
    width: 535px;
    background: var(--white);
    overflow: hidden;
  }
  .card--front { left: 333px; top: 178px; height: 305px; }
  .card--back  { left: 333px; top: 515px; height: 307px; }
  .card__shapes { position: absolute; inset: 0; width: 100%; height: 100%; }

  .wordmark {
    position: absolute;
    color: var(--navy);
    font-weight: 700;
    line-height: 1;
    text-align: center;
  }
  .wordmark__name { display: block; letter-spacing: 0.02em; }
  .wordmark__sub  { display: block; letter-spacing: 0.32em; }
  .card--front .wordmark { left: 14px; top: 24px; }
  .card--front .wordmark__name { font-size: 30px; }
  .card--front .wordmark__sub  { font-size: 9px; margin-top: 3px; }
  .card--back .wordmark { left: 0; right: 0; top: 88px; }
  .card--back .wordmark__name { font-size: 52px; }
  .card--back .wordmark__sub  { font-size: 14px; margin-top: 6px; padding-left: 0.32em; }

  .person { position: absolute; left: 13px; top: 116px; color: var(--navy); }
  .person__name  { font-size: 20px; font-weight: 700; line-height: 1.1; }
  .person__title { font-size: 13px; font-weight: 600; margin-top: 3px; }

  .contact {
    position: absolute; left: 314px; top: 150px;
    color: var(--white); font-size: 12.5px; font-weight: 500; line-height: 15.5px;
    letter-spacing: 0.015em;
  }
  .contact__license { color: var(--green); font-size: 14px; line-height: 19px; margin-top: 2px; }
  .contact__direct { margin-top: 22px; line-height: 18px; }
</style>
</head>
<body>

<section class="card card--front" aria-label="Business card front">
  <svg class="card__shapes" viewBox="0 0 535 305" preserveAspectRatio="none" aria-hidden="true">
    <polygon points="359,0 535,0 535,305 199,305" fill="var(--navy)"/>
    <line x1="357" y1="0" x2="197" y2="305" stroke="var(--green)" stroke-width="4"/>
  </svg>

  <div class="wordmark">
    <span class="wordmark__name">HALDEN</span>
    <span class="wordmark__sub">CONSTRUCTION</span>
  </div>

  <div class="person">
    <p class="person__name">Paul Merriton</p>
    <p class="person__title">President</p>
  </div>

  <div class="contact">
    <p>4700 Calloway Lane Suite 305</p>
    <p>Cedar Bay Gardens, FL 33918</p>
    <p>www.haldenbuilds.com</p>
    <p class="contact__license">CGC 374915</p>
    <div class="contact__direct">
      <p>Office: (555) 284-3916</p>
      <p>Cell: (555) 431-0827</p>
      <p>paulm@haldenbuilds.com</p>
    </div>
  </div>
</section>

<section class="card card--back" aria-label="Business card back">
  <svg class="card__shapes" viewBox="0 0 535 307" preserveAspectRatio="none" aria-hidden="true">
    <polygon points="0,0 36,0 196,307 0,307" fill="var(--navy)"/>
    <line x1="38" y1="0" x2="198" y2="307" stroke="var(--green)" stroke-width="4"/>
    <polygon points="499,0 535,0 535,307 339,307" fill="var(--navy)"/>
    <line x1="497" y1="0" x2="337" y2="307" stroke="var(--green)" stroke-width="4"/>
  </svg>

  <div class="wordmark">
    <span class="wordmark__name">HALDEN</span>
    <span class="wordmark__sub">CONSTRUCTION</span>
  </div>
</section>

</body>
</html>
```